Bright Haven Estate Sales web design

We are looking to launch an Estate Sales Website for Nashville, TN. The name of our Business is Bright Haven Estate Sales. We would like to give you a blank slate so that you can showcase your design skills for us. The few things we are looking for are a nice header graphic of a house or a stock image of an estate sale. Near the header graphic we would like a quick inquiry form. If not on the right side of the header maybe midway down the site. We potentially want to see what purple and Gold look like on the site however this is not a must. We have over 20 years of industry related experience.

1. Buttons at top of the website will be.
a. Services
b. Upcoming Sales
c. About Us
d. FAQs
e. Resources

Services we offer:
1. Estate Sales
2. Cleanouts
3. Appraisals

Sites We like:
https://www.corvellestatesales.example/

We don't have a logo yet so if you have ideas please share them with us. Below are 2 ideas however if you have your own thoughts please ignore.

1. Oval ornate frame, gold and black, with BHES in the middle, deep purple. Think of catering to high class people..font should be fancy as opposed to simple.

2. Another option, Bright Haven in bold fancy script, same colors, with Estate Sales below, small different font, black.

```html
<!DOCTYPE html>
<html lang="en">
<head>
<meta charset="utf-8">
<title>Bright Haven Estate Sales</title>
<link href="https://fonts.googleapis.com/css2?family=Almendra:wght@700&family=Montserrat:wght@400;500;600&display=swap" rel="stylesheet">
<style>
:root{
  --purple:#5e0b69;
  --purple-deep:#3e0a48;
  --lilac:#e3d7e3;
  --lilac-soft:#ebe2ea;
  --gold:#d8b43c;
  --page:#f6f2f4;
  --ink:#1f1a22;
  --muted:#8a8390;
  --white:#ffffff;
}
*{box-sizing:border-box;margin:0;padding:0}
html,body{width:1200px;height:4981px;overflow:hidden}
body{background:var(--page);font-family:"Montserrat",sans-serif;color:var(--ink);position:relative}
.abs{position:absolute}
.display{font-family:"Almendra",serif;font-weight:700;color:var(--purple)}
.photo{position:absolute;display:block}
.btn-outline{position:absolute;border:1.5px solid var(--purple);color:var(--purple);font-size:15px;display:flex;align-items:center;justify-content:center;gap:14px;border-radius:3px}
.arrow{width:26px;height:10px}

/* hero */
.hero{left:0;top:0;width:1200px;height:711px;background:linear-gradient(180deg,#5a5f86 0%,#7a7a9a 35%,#4a4540 75%,#2f3a2a 100%)}
.nav{left:120px;top:68px;width:1005px;height:95px;background:var(--white);border-radius:14px;box-shadow:0 4px 18px rgba(0,0,0,.15)}
.nav a{position:absolute;top:38px;font-size:15px;color:#4a4450;text-decoration:none}
.nav a.active{color:var(--ink);font-weight:600}
.logo-badge{left:73px;top:35px;width:154px;height:154px;border-radius:50%;background:var(--white);border:5px solid var(--gold);display:flex;align-items:center;justify-content:center;text-align:center;font-size:13px;font-weight:600;color:var(--purple);line-height:1.3}
.hero-title{left:0;width:1200px;top:340px;text-align:center;font-family:"Almendra",serif;font-weight:700;font-size:84px;color:var(--white)}
.hero-sub{left:0;width:1200px;top:440px;text-align:center;font-size:27px;color:var(--white)}
.hero-btn{left:504px;top:487px;width:191px;height:38px;background:var(--purple);color:var(--white);font-size:15px;display:flex;align-items:center;justify-content:center;gap:12px;border-radius:3px}
.dot{top:562px;width:14px;height:14px;border-radius:50%;border:2px solid var(--white)}

/* form */
.inquiry{left:112px;top:595px;width:974px;height:398px;background:var(--purple)}
.inquiry h2{position:absolute;left:88px;top:66px;font-family:"Almendra",serif;font-size:36px;color:var(--white)}
.inquiry .rule{position:absolute;height:1px;background:rgba(255,255,255,.55)}
.field{position:absolute;color:var(--white);font-size:15px;display:flex;align-items:center;gap:12px}
.field svg{width:18px;height:18px}
.inquiry .submit{position:absolute;left:657px;top:280px;width:238px;height:40px;border:1.5px solid var(--white);color:var(--white);font-size:15px;display:flex;align-items:center;justify-content:center;border-radius:3px}

/* deals */
.section-heading{font-size:36px;color:#3a3440}
.deal{top:1120px;width:278px;height:380px;background:var(--white);box-shadow:0 3px 12px rgba(0,0,0,.08)}
.deal .photo{left:0;top:0;width:278px;height:246px}
.deal h3{position:absolute;left:15px;top:262px;font-size:19px;font-weight:500}
.deal p{position:absolute;left:15px;top:300px;width:250px;font-size:14px;color:var(--muted);line-height:22px}

/* story */
.story-band{left:0;top:1584px;width:1200px;height:680px;background:linear-gradient(180deg,#4f3f8e 0%,#3e2f6e 100%)}
.story-card{left:112px;top:1690px;width:491px;height:470px;background:var(--white)}
.story-card .eyebrow{position:absolute;left:32px;top:60px;font-size:13px;color:#555}
.story-card h2{position:absolute;left:32px;top:84px;font-size:38px}
.story-card .lead{position:absolute;left:32px;top:144px;width:300px;font-size:16px;line-height:26px}
.story-card .body{position:absolute;left:32px;top:202px;width:440px;font-size:12.5px;line-height:24px;color:#444}

/* services */
.eyebrow-center{left:0;width:1200px;text-align:center;font-size:14px;color:#555}
.service{top:2492px;width:346px;height:362px}
.service.featured{background:var(--lilac)}
.service svg.icon{position:absolute;left:46px;top:30px;width:52px;height:60px}
.service h3{position:absolute;left:46px;top:106px;font-size:19px;font-weight:500}
.service p{position:absolute;left:46px;top:146px;width:270px;font-size:13px;line-height:24px;color:#555}
.service .btn-outline{left:46px;top:288px;width:150px;height:40px}
.service.featured .btn-outline{background:var(--purple);color:var(--white);box-shadow:0 3px 8px rgba(0,0,0,.25)}

/* process */
.process{left:0;top:2970px;width:1200px;height:711px;background:var(--lilac)}
.process .eyebrow{position:absolute;left:108px;top:78px;font-size:17px;color:var(--purple-deep)}
.process h2{position:absolute;left:108px;top:106px;width:700px;font-size:42px;line-height:50px}
.process h2 span{color:#a493a6}
.step{position:absolute;left:108px;width:350px}
.step .num{position:absolute;left:0;top:0;width:36px;height:32px;border-radius:14px 0 0 14px;background:var(--lilac-soft);font-size:22px;font-weight:500;color:var(--purple-deep);padding-left:8px}
.step h3{position:absolute;left:50px;top:0;font-size:22px;font-weight:500;color:var(--purple-deep)}
.step p{position:absolute;left:52px;top:36px;width:300px;font-size:13px;line-height:19px;color:#555}
.gold-btn{left:110px;top:3574px;width:288px;height:40px;background:var(--gold);color:var(--ink);font-size:15px;display:flex;align-items:center;justify-content:center;gap:24px;box-shadow:0 3px 8px rgba(0,0,0,.25)}

/* articles */
.article{top:3874px;width:230px;height:318px}
.article .photo{left:0;top:0;width:230px;height:192px}
.article h3{position:absolute;left:2px;top:206px;width:228px;font-size:17px;font-weight:500;line-height:25px;color:#a69aa8}
.article.active h3{color:var(--purple)}
.article .more{position:absolute;left:2px;top:302px;font-size:12px;color:#999;display:flex;gap:10px;align-items:center}
.article.active .more{color:var(--ink)}

/* newsletter */
.newsletter{left:0;top:4305px;width:1200px;height:264px;background:linear-gradient(90deg,#3a0a46,#4a0c57)}
.newsletter h2{position:absolute;left:114px;top:108px;font-size:36px;color:var(--white)}
.newsletter .line{position:absolute;left:112px;top:168px;width:976px;height:1px;background:rgba(255,255,255,.5)}
.newsletter .input{position:absolute;left:756px;top:100px;width:250px;height:64px;border:1px solid rgba(255,255,255,.6);color:var(--white);font-size:16px;display:flex;align-items:center;padding-left:34px}
.newsletter .send{position:absolute;left:1006px;top:100px;width:82px;height:64px;background:var(--white);display:flex;align-items:center;justify-content:center}

/* footer */
.footer-logo{left:112px;top:4650px;width:158px;height:178px;border-radius:50%;border:5px solid var(--gold);display:flex;align-items:center;justify-content:center;text-align:center;font-size:14px;font-weight:600;color:var(--purple);line-height:1.35}
.contact{position:absolute;left:350px;font-size:15px;color:#333;line-height:22px;display:flex;gap:18px}
.contact svg{width:14px;height:14px;margin-top:4px;flex:none}
.footer-links{left:718px;top:4671px;font-size:15px;line-height:28.6px;color:var(--purple-deep);list-style:none}
.social{top:4735px;width:26px;height:26px;border-radius:50%;background:var(--ink)}
.footer-rule{left:112px;top:4902px;width:976px;height:1px;background:#d8d0d8}
.copyright{left:0;width:1200px;top:4928px;text-align:center;font-size:12px;color:#333}
</style>
</head>
<body>

<!-- hero -->
<div class="abs hero photo" role="img" aria-label="Modern two-storey house with solar roof at dusk, lit windows and garden"></div>
<div class="abs nav">
  <a class="active" style="left:170px">Home</a>
  <a style="left:251px">Services</a>
  <a style="left:346px">Upcoming Sales</a>
  <a style="left:504px">About Us</a>
  <a style="left:608px">FAQs</a>
  <a style="left:681px">Resources</a>
  <svg class="abs" style="left:794px;top:32px" width="30" height="30" viewBox="0 0 24 24" fill="none" stroke="#1f1a22" stroke-width="1.6"><path d="M5 3h4l2 5-3 2a12 12 0 0 0 6 6l2-3 5 2v4a2 2 0 0 1-2 2A18 18 0 0 1 3 5a2 2 0 0 1 2-2z"/></svg>
  <span class="abs" style="left:844px;top:36px;font-size:19px;font-weight:500">+1 615 555 0142</span>
</div>
<div class="abs logo-badge">Bright Haven<br>Estate Sales</div>
<div class="abs hero-title">BHES</div>
<div class="abs hero-sub">We have over 20 years of industry related experience.</div>
<div class="abs hero-btn">Read More Info
  <svg class="arrow" viewBox="0 0 26 10" fill="none" stroke="#fff" stroke-width="1.6"><path d="M0 5h24M19 1l5 4-5 4"/></svg></div>
<div class="abs dot" style="left:556px;background:rgba(255,255,255,.3);width:18px;height:18px;top:560px"></div>
<div class="abs dot" style="left:582px"></div>
<div class="abs dot" style="left:606px"></div>
<div class="abs dot" style="left:631px"></div>

<!-- inquiry form -->
<form class="abs inquiry">
  <h2>Say Hello!</h2>
  <div class="rule" style="left:292px;top:92px;width:598px"></div>
  <div class="field" style="left:82px;top:148px"><svg viewBox="0 0 20 20" fill="none" stroke="#fff" stroke-width="1.4"><circle cx="10" cy="10" r="8.5"/><circle cx="10" cy="8" r="3"/><path d="M4.5 16c1.5-3 9.5-3 11 0"/></svg>Your Name</div>
  <div class="rule" style="left:82px;top:180px;width:384px"></div>
  <div class="field" style="left:508px;top:148px"><svg viewBox="0 0 20 20" fill="none" stroke="#fff" stroke-width="1.4"><rect x="2" y="4" width="16" height="12"/><path d="M2 4l8 7 8-7"/></svg>Your Email</div>
  <div class="rule" style="left:508px;top:180px;width:388px"></div>
  <div class="field" style="left:82px;top:206px"><svg viewBox="0 0 24 24" fill="none" stroke="#fff" stroke-width="1.6"><path d="M5 3h4l2 5-3 2a12 12 0 0 0 6 6l2-3 5 2v4a2 2 0 0 1-2 2A18 18 0 0 1 3 5a2 2 0 0 1 2-2z"/></svg>Your Phone</div>
  <div class="rule" style="left:82px;top:240px;width:384px"></div>
  <div class="field" style="left:508px;top:208px"><svg viewBox="0 0 20 20" fill="none" stroke="#fff" stroke-width="1.4"><rect x="2" y="4" width="13" height="14"/><path d="M8 12l9-9 1.5 1.5-9 9H8z"/></svg>Questions about Features/Benefits</div>
  <div class="rule" style="left:508px;top:240px;width:388px"></div>
  <div class="rule" style="left:82px;top:300px;width:534px"></div>
  <div class="submit">Schedule a Consultation</div>
</form>

<!-- newest deals -->
<h2 class="abs section-heading" style="left:110px;top:1068px;font-weight:400">Newest <span style="font-weight:500">Deals</span></h2>
<div class="abs deal" style="left:112px"><div class="photo" role="img" aria-label="Two-storey suburban home with lawn at dusk" style="background:linear-gradient(180deg,#7b8fc0,#9a8e7c 60%,#4f7a3a)"></div><h3>Neque porro quisquam</h3><p>Many desktop publishing packages and web page editors now use Lorem</p></div>
<div class="abs deal" style="left:427px"><div class="photo" role="img" aria-label="Lit family home with porch and front garden at evening" style="background:linear-gradient(180deg,#5a6a9a,#a88f6a 60%,#3d6b30)"></div><h3>Neque porro quisquam</h3><p>Many desktop publishing packages and web page editors now use Lorem</p></div>
<div class="abs deal" style="left:744px"><div class="photo" role="img" aria-label="Bright living room with wooden floor and staircase" style="background:linear-gradient(180deg,#eeeae6,#d8d0c8 55%,#7a4a2a)"></div><h3>Neque porro quisquam</h3><p>Many desktop publishing packages and web page editors now use Lorem</p></div>
<div class="abs deal" style="left:1061px"><div class="photo" role="img" aria-label="Cottage-style house with flower garden" style="background:linear-gradient(180deg,#a9c6e0,#c8c2b4 55%,#5a8a3a)"></div><h3>Neque porro quisquam</h3><p>Many desktop publishing packages and web page editors now use Lorem</p></div>

<!-- our story -->
<div class="abs story-band photo" role="img" aria-label="City skyline at dusk under a purple tint"></div>
<div class="abs story-card">
  <div class="eyebrow">Our Story</div>
  <h2 class="display">Bright Haven Estate Sales</h2>
  <div class="lead">We have over <b>20 years</b> of industry related experience.</div>
  <div class="body">There are many variations of passages of Lorem Ipsum available, but the majority have suffered alteration in some form, by injected humour, or randomised words which don't look even slightly believable. If you are going to use a passage of Lorem Ipsum, you need to be sure there isn't anything embarrassing hidden in the middle of text.</div>
  <div class="btn-outline" style="left:34px;top:368px;width:184px;height:40px">More info <svg class="arrow" viewBox="0 0 26 10" fill="none" stroke="currentColor" stroke-width="1.6"><path d="M0 5h24M19 1l5 4-5 4"/></svg></div>
</div>
<div class="photo" role="img" aria-label="Estate agents reviewing a tablet with a client" style="left:603px;top:1690px;width:485px;height:470px;background:linear-gradient(120deg,#6a5a4a,#b8a890 50%,#3a3432)"></div>

<!-- services -->
<div class="abs eyebrow-center" style="top:2388px">Services we offer</div>
<h2 class="abs display" style="left:0;width:1200px;text-align:center;top:2414px;font-size:40px">Bright Haven Estate Sales</h2>
<div class="abs service" style="left:66px">
  <svg class="icon" viewBox="0 0 52 60" fill="none" stroke="#5e0b69" stroke-width="2"><path d="M46 2v56M4 8h42"/><rect x="4" y="16" width="34" height="20"/><text x="9" y="30" font-size="10" font-family="Montserrat" fill="#5e0b69" stroke="none" font-weight="600">SALE</text></svg>
  <h3>Estate Sales</h3>
  <p>Contrary to popular belief, Lorem Ipsum is not simply random text. It has roots in a piece of classical Latin literature from 45 BC, making it over 2000 years old.</p>
  <div class="btn-outline">More info <svg class="arrow" viewBox="0 0 26 10" fill="none" stroke="currentColor" stroke-width="1.6"><path d="M0 5h24M19 1l5 4-5 4"/></svg></div>
</div>
<div class="abs service featured" style="left:427px">
  <svg class="icon" viewBox="0 0 52 60" fill="none" stroke="#5e0b69" stroke-width="2"><path d="M12 28l14-12 14 12M16 25v12h20V25"/><path d="M4 50c8-6 14-6 22-2h10l10-6"/><path d="M26 4v6M14 8l3 5M38 8l-3 5"/></svg>
  <h3>Clean-outs</h3>
  <p>Contrary to popular belief, Lorem Ipsum is not simply random text. It has roots in a piece of classical Latin literature from 45 BC, making it over 2000 years old.</p>
  <div class="btn-outline">More info <svg class="arrow" viewBox="0 0 26 10" fill="none" stroke="currentColor" stroke-width="1.6"><path d="M0 5h24M19 1l5 4-5 4"/></svg></div>
</div>
<div class="abs service" style="left:788px">
  <svg class="icon" viewBox="0 0 52 60" fill="none" stroke="#5e0b69" stroke-width="2"><path d="M4 26L26 6l22 20M10 22v30h32V22"/><circle cx="26" cy="36" r="8"/><path d="M26 31v10"/></svg>
  <h3>Appraisals</h3>
  <p>Contrary to popular belief, Lorem Ipsum is not simply random text. It has roots in a piece of classical Latin literature from 45 BC, making it over 2000 years old.</p>
  <div class="btn-outline">More info <svg class="arrow" viewBox="0 0 26 10" fill="none" stroke="currentColor" stroke-width="1.6"><path d="M0 5h24M19 1l5 4-5 4"/></svg></div>
</div>

<!-- process -->
<div class="abs process">
  <div class="eyebrow">Our Process</div>
  <h2 class="display">Neque porro quisquam est qui <span>dolorem ipsum quia,</span></h2>
</div>
<div class="step" style="top:3216px"><div class="num">01</div><h3>Neque porro quisquam</h3><p>It is a long established fact that a reader will be distracted by the readable content of a page when looking at its layout.</p></div>
<div class="step" style="top:3336px"><div class="num">02</div><h3>Neque porro</h3><p>It is a long established fact that a reader will be distracted by the readable content of a page when looking at its layout.</p></div>
<div class="step" style="top:3458px"><div class="num">03</div><h3>Porro quisquam</h3><p>It is a long established fact that a reader will be distracted by the readable content of a page when looking at its layout.</p></div>
<div class="abs gold-btn">Schedule a Consultation <svg width="36" height="14" viewBox="0 0 36 14" fill="none" stroke="#1f1a22" stroke-width="2"><path d="M0 7h34M27 1l7 6-7 6"/></svg></div>
<div class="photo" role="img" aria-label="Agent on a phone call in an office, with play button for video" style="left:479px;top:3242px;width:323px;height:367px;border-radius:8px;background:linear-gradient(160deg,#b9a3bd,#7d5f85)"></div>
<svg class="abs" style="left:616px;top:3400px" width="48" height="48" viewBox="0 0 48 48" fill="none" stroke="#fff" stroke-width="2"><circle cx="24" cy="24" r="22"/><path d="M19 15l13 9-13 9z" fill="#fff"/></svg>
<div class="photo" role="img" aria-label="Colleagues working at desks in a glass-walled office" style="left:831px;top:3033px;width:255px;height:576px;border-radius:8px;background:linear-gradient(180deg,#c8bccc,#9e8aa4)"></div>

<!-- articles -->
<h2 class="abs display" style="left:0;width:1200px;text-align:center;top:3784px;font-size:40px">Our Latest Article</h2>
<div class="abs" style="left:555px;top:3850px;width:90px;height:3px;background:var(--purple)"></div>
<div class="abs article" style="left:112px"><div class="photo" role="img" aria-label="Family in a bright empty home with large windows" style="background:linear-gradient(180deg,#e6e8ec,#c8b8a4)"></div><h3>Neque porro quisquam qui dolorem ipsum quia dolor sit amet,</h3><div class="more">Read More <svg width="16" height="8" viewBox="0 0 16 8" fill="none" stroke="currentColor"><path d="M0 4h14M11 1l3 3-3 3"/></svg></div></div>
<div class="abs article" style="left:361px"><div class="photo" role="img" aria-label="Suburban house with lawn" style="background:linear-gradient(180deg,#7b8fc0,#a8967c 60%,#4f7a3a)"></div><h3>Neque porro quisquam qui dolorem ipsum quia dolor sit amet,</h3><div class="more">Read More <svg width="16" height="8" viewBox="0 0 16 8" fill="none" stroke="currentColor"><path d="M0 4h14M11 1l3 3-3 3"/></svg></div></div>
<div class="abs article active" style="left:611px"><div class="photo" role="img" aria-label="Couple unpacking in a new kitchen" style="background:linear-gradient(180deg,#e8e4e0,#a08a98)"></div><h3>Neque porro quisquam qui dolorem ipsum quia dolor sit amet,</h3><div class="more">Read More <svg width="16" height="8" viewBox="0 0 16 8" fill="none" stroke="currentColor"><path d="M0 4h14M11 1l3 3-3 3"/></svg></div></div>
<div class="abs article" style="left:860px"><div class="photo" role="img" aria-label="Hands signing a contract at a desk" style="background:linear-gradient(180deg,#3a4a5c,#8a7060)"></div><h3>Neque porro quisquam qui dolorem ipsum quia dolor sit amet,</h3><div class="more">Read More <svg width="16" height="8" viewBox="0 0 16 8" fill="none" stroke="currentColor"><path d="M0 4h14M11 1l3 3-3 3"/></svg></div></div>

<!-- newsletter -->
<div class="abs newsletter">
  <h2 class="display" style="color:#fff">Subscribe Our Newsletter</h2>
  <div class="line"></div>
  <div class="input">Email Address</div>
  <div class="send"><svg width="24" height="24" viewBox="0 0 24 24" fill="#3e0a48"><path d="M22 2L2 10l7 3 3 9z"/></svg></div>
</div>

<!-- footer -->
<div class="abs footer-logo">Bright Haven<br>Estate Sales</div>
<div class="contact" style="top:4684px"><svg viewBox="0 0 14 14" fill="#333"><path d="M7 0a5 5 0 0 1 5 5c0 4-5 9-5 9S2 9 2 5a5 5 0 0 1 5-5z"/><circle cx="7" cy="5" r="2" fill="#fff"/></svg><span>Bright Haven Estate Sales<br>418 Maple Crest Lane, Franklin,<br>TN 37064</span></div>
<div class="contact" style="top:4758px"><svg viewBox="0 0 24 24" fill="#333"><path d="M5 3h4l2 5-3 2a12 12 0 0 0 6 6l2-3 5 2v4a2 2 0 0 1-2 2A18 18 0 0 1 3 5a2 2 0 0 1 2-2z"/></svg><span>+1 615 555 0142</span></div>
<div class="contact" style="top:4788px"><svg viewBox="0 0 14 14" fill="none" stroke="#333"><rect x="1" y="3" width="12" height="9"/><path d="M1 3l6 5 6-5"/></svg><span>hello@brighthaven.example</span></div>
<ul class="abs footer-links"><li>Home</li><li>Services</li><li>Upcoming Sales</li><li>About Us</li><li>FAQs</li><li>Resources</li></ul>
<div class="abs social" style="left:946px" aria-label="Social link"></div>
<div class="abs social" style="left:982px" aria-label="Social link"></div>
<div class="abs social" style="left:1018px" aria-label="Social link"></div>
<div class="abs social" style="left:1054px" aria-label="Social link"></div>
<div class="abs footer-rule"></div>
<div class="abs copyright">Bright Haven Estate Sales © 2024 All Rights Reserved.</div>

</body>
</html>
```